Step Boldly Toward Gain Promotional Flyer

I Need a one page, one-sided 8.5 x 11 editable promotional flyer that POPS!, designed in photoshop

[TITLE]Step Boldly Toward Gain: 3 BOLD Moves to Up-Level Your Business Now!

[CONTENT for the Flyer:]

At this content-rich event you will learn how to:
• Get out of feast and famine mode and into six, multi-six and/or seven figure-income mode
• Leapfrog your competition and become the obvious choice in your market
• Have your business aligned with who you are and what you want
• Enjoy your business far more than you imagined possible.
• Have more fun and time to yourself
• Live free and unbound!

Accolades
“Delphine helped us increase our six figure income by 41%...I feel reborn!” Marlene & Otis Pruitt, Vienna, VA

“…Delphine is a joy to listen to - compelling, smart, provocative…” – Dennis Ashcombe, Charlotte, North Carolina

“Delphine helped me increase my business by 66%...without me spending more time, money, or making cold calls! …I am in the zone!” Tina Worsley, Baltimore, MD
“Delphine is an energetic and dynamic speaker…content-rich…holds your attention to the very end!” Neil Barrow, Frmr Pres., Crane & Whitby, MD, MD, D.C., PA, DE, NJ
“Delphine is the real estate whisperer!” Hal Drummond, Washington D.C.

“Delphine was prepared, funny, informative and made a connection with each of our agents…Fabulous!…even my admins were PUMPED!!! – Paul Venable, New York

About Delphine:
Delphine is a highly regarded business development speaker & coach who knows how to pump up an audience and have them making more money, in less time, AND having more fun doing it! What’s not to love?! Consistently rated as an exceptional speaker and conference favorite! Among her work: Standout Method: How to Draw Your Best Buyers Time after Time!, Contact Sourcing Done Easy, The Worst Outreach Errors Real Estate Agents Commit and How to Steer Clear of Them, Slow Seasons Build Sharp Sellers, Drive Within the Head for Real Estate Agents.

[Also need a section for:]
Date: December 9, 2015, Time: 9:00 Am - 12:00 Noon, Place: Harbor Lantern Convention, Green Castle, PA

Target Market(s)

Real Estate Agents

Industry/Entity Type

Real Estate Agent

Font styles to use
Sans Serif

Colors
0655a3
f37122

Requirements
Must have
• the peak tier realty mentor logo
Nice to have
• step boldly toward gain logo; lots of POP! :-) ; open to other colors, accent colors.

```html
<!DOCTYPE html>
<html lang="en">
<head>
<meta charset="utf-8">
<title>Step Boldly Toward Gain – Event Flyer</title>
<link href="https://fonts.googleapis.com/css2?family=Anton&family=Lato:ital,wght@0,300;0,400;0,700;0,900;1,300;1,400;1,700&display=swap" rel="stylesheet">
<style>
  :root{
    --brand-blue:#0655a3;
    --brand-orange:#f37122;
    --navy:#1d2a5c;
    --ink:#1c1c1c;
    --body-text:#4a4a4a;
    --paper:#ffffff;
    --mist:#e9eaec;
    --stage:#d9d6d2;
  }
  *{box-sizing:border-box;margin:0;padding:0}
  html,body{width:900px;height:1200px;overflow:hidden;background:var(--stage)}
  .canvas{position:relative;width:900px;height:1200px;overflow:hidden}
  .flyer{
    position:absolute;left:21px;top:47px;width:715px;height:922px;
    transform:scale(1.2);transform-origin:0 0;
    background:linear-gradient(180deg,var(--paper) 0%,#f4f4f5 45%,var(--mist) 75%);
    font-family:"Lato",sans-serif;overflow:hidden;
    box-shadow:0 4px 14px rgba(0,0,0,.25);
  }
  .flyer-shapes{position:absolute;inset:0;width:715px;height:922px}

  .headline{position:absolute;left:30px;top:24px;font-family:"Anton",sans-serif;line-height:1}
  .headline .kicker{display:block;font-size:30px;color:var(--ink);letter-spacing:.2px}
  .headline .moves{display:block;font-size:24px;color:var(--paper);margin-top:6px}
  .headline .main{display:block;font-size:40px;color:var(--ink);margin-top:5px}

  .brand-mark{position:absolute;left:462px;top:42px;white-space:nowrap;
    font-family:"Lato",sans-serif;font-weight:700;font-size:20px;color:var(--navy);line-height:1}

  .benefits{position:absolute;top:230px;list-style:none;font-size:12px;font-style:italic;font-weight:300;color:var(--body-text);line-height:1.3}
  .benefits li{position:relative;padding-left:10px}
  .benefits li::before{content:"";position:absolute;left:0;top:6px;width:5px;height:5px;border-radius:50%;background:var(--brand-orange)}
  .benefits--left{left:38px;width:420px}
  .benefits--right{left:470px;width:205px}

  .accolades{position:absolute;left:38px;top:322px;width:640px}
  .accolades h2{font-size:17px;font-weight:700;color:var(--brand-orange)}
  .accolades ul{list-style:none;margin-top:6px}
  .accolades li{position:relative;padding-left:10px;font-size:11.4px;font-style:italic;font-weight:300;color:var(--body-text);line-height:1.4;margin-bottom:12px}
  .accolades li::before{content:"";position:absolute;left:0;top:6px;width:5px;height:5px;border-radius:50%;background:var(--brand-orange)}

  .about{position:absolute;left:40px;top:655px;width:436px;color:var(--paper)}
  .about h2{font-size:24px;font-weight:700;color:var(--brand-orange)}
  .about p{margin-top:10px;font-size:10px;font-style:italic;font-weight:300;line-height:1.4}

  .event{position:absolute;left:44px;top:795px;color:var(--paper)}
  .event-row{display:flex;align-items:baseline;height:22px}
  .event-row dt{width:64px;font-size:16px;font-weight:700;font-style:italic;color:var(--brand-orange)}
  .event-row dd{font-size:15px;font-weight:700}

  .speaker-photo{position:absolute;left:490px;top:640px;width:214px;height:232px}
</style>
</head>
<body>
<div class="canvas">
  <article class="flyer">
    <svg class="flyer-shapes" viewBox="0 0 715 922" aria-hidden="true">
      <defs>
        <linearGradient id="orangeFill" x1="0" y1="0" x2="0" y2="1">
          <stop offset="0" stop-color="#f37122"/>
          <stop offset="1" stop-color="#f7941d"/>
        </linearGradient>
        <linearGradient id="blueFill" x1="0" y1="0" x2="0" y2="1">
          <stop offset="0" stop-color="#1d72c9"/>
          <stop offset="1" stop-color="#0655a3"/>
        </linearGradient>
      </defs>
      <path d="M0 0 H345 C400 60 440 120 520 140 C600 158 660 158 715 158 V166 C500 158 230 168 0 230 Z" fill="url(#orangeFill)"/>
      <path d="M345 0 H362 C415 60 455 115 530 134 C600 150 660 152 715 152 V158 C660 158 600 158 520 140 C440 120 400 60 345 0 Z" fill="var(--brand-blue)"/>
      <path d="M0 218 C230 158 500 152 715 160 V168 C500 160 230 170 0 230 Z" fill="var(--brand-blue)"/>
      <ellipse cx="360" cy="440" rx="300" ry="110" fill="#dfe1e4" opacity=".55" role="img" aria-label="faint world map backdrop"/>
      <rect x="28" y="315" width="660" height="265" rx="14" fill="none" stroke="var(--brand-blue)" stroke-width="1.5"/>
      <path d="M0 608 C220 615 470 640 715 628 V878 H0 Z" fill="url(#blueFill)"/>
      <path d="M0 602 C220 612 470 636 715 622 V630 C470 644 220 620 0 614 Z" fill="var(--brand-orange)"/>
      <rect x="0" y="872" width="715" height="4" fill="var(--paper)"/>
      <rect x="0" y="878" width="715" height="44" fill="url(#orangeFill)"/>
    </svg>

    <header class="headline">
      <span class="kicker">Step Boldly Toward Gain</span>
      <span class="moves">3 BOLD Moves to Up-Level</span>
      <span class="main">Your Business Now!</span>
    </header>

    <div class="brand-mark">Step Boldly Toward Gain</div>

    <ul class="benefits benefits--left">
      <li>Get out of feast and famine mode and into six,<br>multi-six and/or seven figure-income mode</li>
      <li>Leapfrog your competition and become the obvious choice in your market</li>
      <li>Have your business aligned with who you are &amp; what you want</li>
    </ul>
    <ul class="benefits benefits--right">
      <li>Enjoy your business far more than you imagined possible.</li>
      <li>Have more fun and time to yourself</li>
      <li>Live free and unbound!</li>
    </ul>

    <section class="accolades">
      <h2>Accolades:</h2>
      <ul>
        <li>Delphine helped us increase our six figure income by 41%...I feel reborn!” Marlene &amp; Otis Pruitt, Vienna, VA</li>
        <li>“…Delphine is a joy to listen to - compelling, smart, provocative…” – Dennis Ashcombe, Charlotte, North Carolina</li>
        <li>“Delphine helped me increase my business by 66%...without me spending more time, money, or making cold calls! …I am in the zone!” Tina Worsley, Baltimore, MD</li>
        <li>“Delphine is an energetic and dynamic speaker…content-rich…holds your attention to the very end!” Neil Barrow, Frmr Pres., Crane &amp; Whitby, MD, MD, D.C., PA, DE, NJ</li>
        <li>“Delphine is the real estate whisperer!” Hal Drummond, Washington D.C.</li>
        <li>“Delphine was prepared, funny, informative and made a connection with each of our agents…Fabulous!…even my admins were PUMPED!!! – Paul Venable, New York</li>
      </ul>
    </section>

    <section class="about">
      <h2>About Delphine:</h2>
      <p>Delphine is a highly regarded business development speaker &amp; coach who knows how to pump up an audience and have them making more money, in less time, AND having more fun doing it! What’s not to love?! Consistently rated as an exceptional speaker and conference favorite! Among her work: Standout Method: How to Draw Your Best Buyers Time after Time!, Contact Sourcing Done Easy, The Worst Outreach Errors Real Estate Agents Commit and How to Steer Clear of Them, Slow Seasons Build Sharp Sellers, Drive Within the Head for Real Estate Agents.</p>
    </section>

    <dl class="event">
      <div class="event-row"><dt>Date:</dt><dd>December 9, 2015,</dd></div>
      <div class="event-row"><dt>Time:</dt><dd>9:00 Am - 12:00 Noon,</dd></div>
      <div class="event-row"><dt>Place:</dt><dd>Harbor Lantern Convention, Green Castle, PA</dd></div>
    </dl>

    <svg class="speaker-photo" viewBox="0 0 214 232" role="img" aria-label="Portrait photo of speaker Delphine in a dark blazer">
      <defs>
        <linearGradient id="photoTone" x1="0" y1="0" x2="0" y2="1">
          <stop offset="0" stop-color="#3f86d0"/>
          <stop offset=".55" stop-color="#c9a98e"/>
          <stop offset="1" stop-color="#2a2a2e"/>
        </linearGradient>
      </defs>
      <rect width="214" height="232" fill="url(#photoTone)" opacity=".85"/>
    </svg>
  </article>
</div>
</body>
</html>
```